ROLL-UP DESIGN FOR SUPERMARKET DELIVERY

We need the graphic design of a roll-up with measurements 200 cm height x cm 85 width, for a supermarket delivery service.

The main logo "The Velarno" either color version or black version must be present very visible on the design.

the second logo attached 'CALVESINOSHOP' must also be present but smaller on the design.

the following text must be present on the design: CONSEGNA STESSO GIORNO.

Printing instruction attached must be respected.

Target Market(s)

HIGH END ITALIAN AND EUROPEAN SUPERMARKET CLIENTELE

Industry/Entity Type

FOOD DELIVERY

Requirements
Must have
• LOGOS ATTACHED
Nice to have
• PHOTOS OF SEA, SARDINIA, LUXURY DELIVERY, YACHTS

```html
<!DOCTYPE html>
<html lang="it">
<head>
<meta charset="utf-8">
<title>The Velarno – Roll-up Consegna Stesso Giorno</title>
<link rel="stylesheet" href="https://fonts.googleapis.com/css2?family=Montserrat:wght@600;700;800&display=swap">
<style>
  :root {
    --sun-yellow: #F7C242;
    --ink: #111111;
    --white: #FFFFFF;
    --bar-tint: rgba(255, 255, 255, 0.22);
    --stand-grey: #97989C;
  }
  * { margin: 0; padding: 0; box-sizing: border-box; }
  html, body { width: 1200px; height: 3102px; overflow: hidden; }
  body { background: var(--sun-yellow); font-family: "Montserrat", Arial, sans-serif; }

  .rollup { position: relative; width: 1200px; height: 3102px; background: var(--sun-yellow); overflow: hidden; }

  .photo-layer { position: absolute; left: 0; top: 0; width: 1200px; height: 3102px; }

  .brand-lockup {
    position: absolute; top: 88px; right: 82px;
    display: flex; align-items: center; gap: 28px;
  }
  .brand-dot {
    width: 72px; height: 72px; border-radius: 50%;
    border: 6px solid var(--ink); flex: none;
  }
  .brand-text { display: flex; flex-direction: column; align-items: center; }
  .brand-name {
    font-weight: 700; font-size: 92px; line-height: 1;
    color: var(--ink); white-space: nowrap;
  }
  .brand-tagline {
    margin-top: 14px;
    font-weight: 600; font-size: 30px; line-height: 1;
    color: var(--ink); white-space: nowrap;
  }

  .accent-bar { position: absolute; height: 44px; background: var(--bar-tint); }
  .accent-bar.top-1 { left: 992px; top: 435px; width: 106px; }
  .accent-bar.top-2 { left: 782px; top: 529px; width: 316px; }
  .accent-bar.top-3 { left: 929px; top: 623px; width: 169px; }
  .accent-bar.low-1 { left: 298px; top: 2282px; width: 106px; }
  .accent-bar.low-2 { left: 88px;  top: 2376px; width: 316px; }
  .accent-bar.low-3 { left: 236px; top: 2471px; width: 168px; }

  .headline {
    position: absolute; left: 116px; top: 1268px;
    font-weight: 800; font-size: 158px; line-height: 166px;
    letter-spacing: -1px; color: var(--white);
  }
  .headline span { display: block; }

  .partner-shop { position: absolute; left: 66px; top: 2660px; }
  .partner-name {
    font-weight: 700; font-size: 44px; line-height: 1;
    color: var(--ink); white-space: nowrap;
  }
  .partner-tagline {
    margin-top: 8px;
    font-weight: 600; font-size: 20px; line-height: 1;
    color: var(--ink); white-space: nowrap;
  }

  .stand-base { position: absolute; left: 0; top: 2814px; width: 1200px; height: 288px; background: var(--stand-grey); }
</style>
</head>
<body>
<main class="rollup">

  <svg class="photo-layer" viewBox="0 0 1200 3102" xmlns="http://www.w3.org/2000/svg">
    <defs>
      <linearGradient id="seafront-tone" x1="0" y1="0" x2="0" y2="1">
        <stop offset="0" stop-color="#4F9560"/>
        <stop offset="0.45" stop-color="#9AAE55"/>
        <stop offset="0.58" stop-color="#3E9A86"/>
        <stop offset="0.68" stop-color="#C99A4E"/>
        <stop offset="1" stop-color="#B57C3A"/>
      </linearGradient>
      <linearGradient id="coast-tone" x1="0" y1="0" x2="0" y2="1">
        <stop offset="0" stop-color="#8C9858"/>
        <stop offset="0.3" stop-color="#BE9E55"/>
        <stop offset="0.65" stop-color="#4E8A66"/>
        <stop offset="1" stop-color="#5E7A4A"/>
      </linearGradient>
      <radialGradient id="open-sea-tone" cx="0.5" cy="0.5" r="0.6">
        <stop offset="0" stop-color="#37B2CB"/>
        <stop offset="1" stop-color="#1C7F9E"/>
      </radialGradient>
    </defs>

    <path role="img" aria-label="Foto: terrazza in legno con panchine affacciata sul mare al tramonto"
      fill="url(#seafront-tone)" fill-rule="evenodd"
      d="M -405 748 a501 501 0 1 0 1002 0 a501 501 0 1 0 -1002 0 Z
         M -126 748 a225 225 0 1 0 450 0 a225 225 0 1 0 -450 0 Z"/>

    <path role="img" aria-label="Foto: scogliera della costa sarda vista dall'alto con acqua turchese"
      fill="url(#coast-tone)" fill-rule="evenodd"
      d="M 599 2157 a500 500 0 1 0 1000 0 a500 500 0 1 0 -1000 0 Z
         M 875 2157 a226 226 0 1 0 452 0 a226 226 0 1 0 -452 0 Z"/>

    <circle role="img" aria-label="Foto: yacht di lusso in navigazione sul mare blu, vista dall'alto"
      cx="1101" cy="2157" r="226" fill="url(#open-sea-tone)"/>
  </svg>

  <header class="brand-lockup">
    <div class="brand-dot"></div>
    <div class="brand-text">
      <div class="brand-name">The Velarno</div>
      <div class="brand-tagline">Consegne su misura</div>
    </div>
  </header>

  <div class="accent-bar top-1"></div>
  <div class="accent-bar top-2"></div>
  <div class="accent-bar top-3"></div>

  <h1 class="headline">
    <span>CONSEGNA</span>
    <span>STESSO</span>
    <span>GIORNO</span>
  </h1>

  <div class="accent-bar low-1"></div>
  <div class="accent-bar low-2"></div>
  <div class="accent-bar low-3"></div>

  <div class="partner-shop">
    <div class="partner-name">Calvesinoshop</div>
    <div class="partner-tagline">La spesa di fiducia</div>
  </div>

  <div class="stand-base"></div>
</main>
</body>
</html>
```